Business card for home decor store and design

I need a business card for my home decor boutique that’s professional looking boho/rustic. We sell vintage furniture, vintage finds, lamps, throws, rugs. We also carry a Diy paint line for refinishing furniture. We offer workshop on painting furniture, private or group setting. We in the heart of Old Town Red Bluff. We love to design, build and restore. Family owned small business. Our style is rustic boho farmhouse. We search for one of a kind found and repurposed items. We love vintage home decor, vintage windows.

Target Market(s)

Home decor

Industry/Entity Type

Home Accessories

Contact Information for Business Card

Have a rustic look/boho

Font styles to use
Serif
Script

Requirements
Must have
• Logo

```html
<!DOCTYPE html>
<html lang="en">
<head>
<meta charset="utf-8">
<title>Birch &amp; Loom Co. — Business Card</title>
<link rel="stylesheet" href="https://fonts.googleapis.com/css2?family=Libre+Baskerville:wght@400;700&display=swap">
<style>
  :root {
    --stage: #2a2a2c;
    --card-dark: #0d0d0e;
    --card-light: #ffffff;
    --ink: #111111;
    --ink-soft: #2b2b2b;
    --silver: #d9d9d9;
    --rule: #3a3a3a;
  }
  * { margin: 0; padding: 0; box-sizing: border-box; }
  html, body { width: 1200px; height: 800px; overflow: hidden; }
  body {
    background: var(--stage);
    font-family: "Libre Baskerville", Georgia, serif;
    position: relative;
  }
  .card {
    position: absolute;
    width: 500px;
    height: 286px;
    border-radius: 22px;
    top: 257px;
  }
  .card--front { left: 70px; background: var(--card-dark); color: var(--silver); }
  .card--back  { left: 630px; background: var(--card-light); color: var(--ink); }

  .brand {
    position: absolute;
    display: flex;
    align-items: center;
    gap: 12px;
    font-size: 19px;
    font-weight: 400;
    white-space: nowrap;
  }
  .brand__dot {
    width: 16px; height: 16px; border-radius: 50%;
    background: currentColor;
    flex: none;
  }
  .card--front .brand { left: 50%; top: 104px; transform: translateX(-50%); }
  .card--back .brand  { left: 32px; top: 130px; }

  .front__web {
    position: absolute;
    left: 0; right: 0; top: 214px;
    text-align: center;
    font-size: 12px;
    letter-spacing: 4px;
  }

  .divider {
    position: absolute;
    left: 262px; top: 44px;
    width: 1px; height: 200px;
    background: var(--rule);
    transform: rotate(-18deg);
  }
  .contact {
    position: absolute;
    left: 296px; top: 66px;
    font-size: 11.5px;
    line-height: 1.45;
    color: var(--ink-soft);
  }
  .contact__name {
    font-weight: 700;
    font-size: 14px;
    letter-spacing: .5px;
    color: var(--ink);
  }
  .contact__role { margin-bottom: 12px; }
  .contact__address { margin-bottom: 12px; }
  .contact__row { display: flex; align-items: center; gap: 8px; }
  .contact__icon { width: 11px; height: 11px; flex: none; }
</style>
</head>
<body>

  <section class="card card--front" aria-label="Card front">
    <div class="brand"><span class="brand__dot"></span>Birch &amp; Loom Co.</div>
    <p class="front__web">www.birchandloom.com</p>
  </section>

  <section class="card card--back" aria-label="Card back">
    <div class="brand"><span class="brand__dot"></span>Birch &amp; Loom Co.</div>
    <span class="divider"></span>
    <div class="contact">
      <p class="contact__name">JONAH REED</p>
      <p class="contact__role">Director</p>
      <p class="contact__address">PO BOX 48, Willow Lane<br>5th street, Ashford</p>
      <p class="contact__row">
        <svg class="contact__icon" viewBox="0 0 12 12"><path d="M2.5 1h2l1 3-1.3 1a6.5 6.5 0 0 0 2.8 2.8L8 6.5l3 1v2A1.5 1.5 0 0 1 9.5 11 8.5 8.5 0 0 1 1 2.5 1.5 1.5 0 0 1 2.5 1z" fill="currentColor"/></svg>
        +1 555 014 772
      </p>
      <p class="contact__row">
        <svg class="contact__icon" viewBox="0 0 12 12"><rect x="0.5" y="2" width="11" height="8" fill="currentColor"/><path d="M0.5 2 6 6.5 11.5 2" fill="none" stroke="#fff" stroke-width="1"/></svg>
        hello@birchandloom.com
      </p>
      <p class="contact__row">
        <svg class="contact__icon" viewBox="0 0 12 12"><circle cx="6" cy="6" r="5.5" fill="currentColor"/><path d="M0.5 6h11M6 .5c-3 3-3 8 0 11M6 .5c3 3 3 8 0 11" fill="none" stroke="#fff" stroke-width=".7"/></svg>
        www.birchandloom.com
      </p>
    </div>
  </section>

</body>
</html>
```